I work in the manufacturing industry and currently for TK in the wind department. I'm a contractor. So no TK symbol can be on the card but I can put a wind turbine on it. I am a skydiver as well, so I want a skydiver in the parachute floating next to a turbine with some clouds, the sun over head and the ground below. Hits the moto.

Quality inspection and manufacturing is the industry I work in.

Industry

Harold Tavisky
MQI (manufacturing Quality Inspector)
"Analyzing Quality from a different angle!"

Lumo48213@mailvista.net
555-382-1974

Must have
• Skydiver in parachute, wind turbine, clouds, the sun and the ground. If you can come up with a better moto, please let me know. The back side display "CobleFen inc" in small text in a corner.

```html
<!DOCTYPE html>
<html lang="en">
<head>
<meta charset="UTF-8">
<title>CobleFen inc – Card Back</title>
<link href="https://fonts.googleapis.com/css2?family=Jura:wght@400&display=swap" rel="stylesheet">
<style>
  :root {
    --sky-top: #0064ac;
    --sky-mid: #003b80;
    --dusk: #1c2a6c;
    --night: #22175b;
    --frame: #1a1a2a;
    --ink-light: #f4f2ff;
  }
  html, body {
    margin: 0;
    padding: 0;
    width: 703px;
    height: 1200px;
    overflow: hidden;
    background: #ffffff;
  }
  .card-back {
    position: relative;
    width: 703px;
    height: 1200px;
    box-sizing: border-box;
    border: 1px solid var(--frame);
    background: linear-gradient(
      to bottom,
      var(--sky-top) 0%,
      var(--sky-mid) 39%,
      var(--dusk) 62%,
      var(--night) 86%,
      var(--night) 100%
    );
  }
  .company-name {
    position: absolute;
    right: 58px;
    bottom: 50px;
    margin: 0;
    font-family: "Jura", "Eurostile", sans-serif;
    font-weight: 400;
    font-size: 23px;
    letter-spacing: 0.2px;
    color: var(--ink-light);
    line-height: 1;
    white-space: nowrap;
  }
</style>
</head>
<body>
  <main class="card-back">
    <p class="company-name">CobleFen inc</p>
  </main>
</body>
</html>
```